Bravo Ledger Path Tracker

Consumers track their three credit scores. I have sent an illustration after one update of their credit scores. Many consumers will have a dozen updates during one year. I would like to show a history of the last 24 months. Put together a design that is attractive and easy to look at and follow. I have updated some ideas for graphs (Apr 5, 2022)

Target Market(s)

Consumers tracking their credit scores

Coding

Coded - Design and coding required

Number of Pages Required

1 page

Colors
0054AA
0677BA
7BADD7
CADEEF
E8F1F8
00AB8E
00BBA5
67D7C9
C6EFE9
E9F9F6

Requirements
Must have
• Scores from 350 to 850 pon the left hand side - dates the credit scores were pulled at the bottom on the x axis
Nice to have
• 3 digit credit score for each of the three scores /

```html
<!DOCTYPE html>
<html lang="en">
<head>
<meta charset="utf-8">
<title>Bravo Ledger Path Tracker – Credit Score History</title>
<link href="https://fonts.googleapis.com/css2?family=Poppins:wght@400;500;600;700&display=swap" rel="stylesheet">
<style>
:root{
  --topbar:#1e86dc;
  --nav:#0b2ad0;
  --white:#ffffff;
  --card-head:#e3edf7;
  --ink:#1d1d1d;
  --muted:#b4b4b4;
  --grid:#d6d6d6;
  --red:#e0141e;
  --green:#129a1a;
  --blue:#1d4fd0;
  --footer-top:#2172d2;
  --footer:#1466c9;
  --dark-btn:#2b2b2b;
}
*{box-sizing:border-box;margin:0;padding:0}
html,body{width:1200px;height:800px;overflow:hidden}
body{position:relative;font-family:'Poppins',sans-serif;background:var(--white);color:var(--ink)}
.topbar{position:absolute;left:0;top:0;width:1200px;height:34px;background:var(--topbar);color:var(--white);font-size:8.5px;font-weight:500}
.topbar .contact{position:absolute;left:53px;top:11px;display:flex;gap:10px;align-items:center}
.topbar .contact span{display:flex;align-items:center;gap:3px}
.login{position:absolute;right:30px;top:4px;width:47px;height:23px;background:var(--dark-btn);font-size:8px;display:flex;align-items:center;justify-content:center}
.navbar{position:absolute;left:0;top:34px;width:1200px;height:66px;background:var(--nav)}
.brand{position:absolute;left:54px;top:22px;display:flex;align-items:center;gap:8px;color:var(--white);font-size:18px;font-weight:500}
.brand i{width:14px;height:14px;background:var(--white);display:block;border-radius:2px}
.menu{position:absolute;right:40px;top:27px;display:flex;gap:20px;color:var(--white);font-size:11px;font-weight:600;align-items:center}
.hero{position:absolute;left:0;top:100px;width:1200px;height:263px;background:linear-gradient(100deg,#3d3a38 0%,#8d8f93 22%,#5a6270 45%,#1d2a3c 60%,#16243a 100%)}
.hero-title{position:absolute;left:53px;top:163px;color:var(--white);font-size:37px;font-weight:700;line-height:39px;letter-spacing:.5px}
.card{position:absolute;left:54px;top:323px;width:1114px;height:342px;background:var(--white);border:1px solid #e4e4e4;border-radius:6px;overflow:hidden}
.card-head{height:40px;background:var(--card-head);padding:11px 15px;font-size:14px;font-weight:500;letter-spacing:.2px}
.chart{position:absolute;left:0;top:363px;width:1200px;height:302px}
.axis-y{position:absolute;left:30px;top:508px;transform:translate(-50%,-50%) rotate(-90deg);font-size:32px;font-weight:700;color:var(--muted);white-space:nowrap}
.axis-x{position:absolute;left:0;width:1222px;top:676px;text-align:center;font-size:30px;font-weight:700;color:var(--muted);letter-spacing:.5px}
.footer{position:absolute;left:0;top:733px;width:1200px;height:67px;background:var(--footer);border-top:24px solid var(--footer-top);color:var(--white);font-size:8.5px}
.footer .copy{position:absolute;left:51px;top:9px}
.footer .addr{position:absolute;left:260px;top:9px}
.social{position:absolute;left:882px;top:1px;display:flex;gap:3px}
.social i{width:23px;height:23px;border-radius:50%;background:#4a7fd8;display:block}
.legal{position:absolute;right:32px;top:9px}
</style>
</head>
<body>
<header class="topbar">
  <div class="contact">
    <span><svg width="7" height="9" viewBox="0 0 7 9"><path d="M3.5 0A3.3 3.3 0 0 0 .2 3.3C.2 5.6 3.5 9 3.5 9s3.3-3.4 3.3-5.7A3.3 3.3 0 0 0 3.5 0zm0 4.6a1.3 1.3 0 1 1 0-2.6 1.3 1.3 0 0 1 0 2.6z" fill="#fff"/></svg>418 Harbor Lane, Suite 210, Millbrook, Oregon 97012</span>
    <span><svg width="8" height="8" viewBox="0 0 8 8"><path d="M1.6.3 2.8 2 2 3.1c.6 1.3 1.6 2.3 2.9 2.9L6 5.2l1.7 1.2-.6 1.3C3.6 7.8.2 4.4.3.9z" fill="#fff"/></svg>(800) 555-0142</span>
  </div>
  <div class="login">LOG IN</div>
</header>
<nav class="navbar">
  <div class="brand"><i></i>Bravo Ledger Path Tracker</div>
  <div class="menu">
    <span>Home</span><span>Testimonials</span><span>Max Scores</span><span>FAQ ▾</span><span>Blog</span>
    <svg width="11" height="11" viewBox="0 0 11 11"><circle cx="4.5" cy="4.5" r="3.3" fill="none" stroke="#fff" stroke-width="1.8"/><path d="M7 7l3 3" stroke="#fff" stroke-width="2"/></svg>
  </div>
</nav>
<section class="hero" role="img" aria-label="Laptop screen showing a credit score gauge in a blurred office setting"></section>
<h1 class="hero-title">Consumers Track<br>History</h1>

<div class="axis-y">Credit Score</div>

<section class="card">
  <div class="card-head">My Credit Score History</div>
</section>

<svg class="chart" viewBox="0 363 1200 302" font-family="Poppins, sans-serif">
  <g stroke="var(--grid)" stroke-width="0.8">
    <line x1="123" y1="411" x2="1051" y2="411"/>
    <line x1="123" y1="463" x2="1051" y2="463"/>
    <line x1="123" y1="515" x2="1051" y2="515"/>
    <line x1="123" y1="568" x2="1051" y2="568"/>
    <line x1="123" y1="411" x2="123" y2="628"/>
    <line x1="123" y1="628" x2="1045" y2="628"/>
  </g>
  <g font-size="11" font-weight="500" fill="var(--ink)" text-anchor="end">
    <text x="113" y="467">701.5</text>
    <text x="113" y="519">685</text>
    <text x="113" y="572">668.5</text>
    <text x="113" y="624">652</text>
  </g>
  <g font-size="11" font-weight="500" fill="var(--ink)" text-anchor="middle">
    <text x="145" y="649">Nov2021</text><text x="213" y="649">Dec2021</text><text x="281" y="649">Jan2022</text><text x="348" y="649">Feb2022</text><text x="416" y="649">Mar2022</text><text x="484" y="649">Apr2022</text><text x="552" y="649">May2022</text><text x="620" y="649">Jun2022</text><text x="688" y="649">Jul2022</text><text x="756" y="649">Aug2022</text><text x="824" y="649">Sep2022</text><text x="892" y="649">Oct2022</text><text x="959" y="649">Nov2022</text><text x="1027" y="649">Dec2022</text>
  </g>
  <line x1="122" y1="572" x2="1047" y2="572" stroke="var(--red)" stroke-width="1.2"/>
  <line x1="122" y1="463" x2="1045" y2="498" stroke="var(--green)" stroke-width="1.2"/>
  <line x1="122" y1="456" x2="1043" y2="508" stroke="var(--blue)" stroke-width="1.2"/>
  <g fill="#fff" stroke="#666" stroke-width="0.8">
    <circle cx="122" cy="572" r="3"/><circle cx="1047" cy="572" r="3"/>
    <circle cx="122" cy="463" r="3"/><circle cx="1045" cy="498" r="3"/>
    <circle cx="122" cy="456" r="3"/><circle cx="1043" cy="508" r="3"/>
  </g>
  <g>
    <rect x="69" y="375" width="106" height="67" rx="6" fill="#fff" style="filter:drop-shadow(0 1px 4px rgba(0,0,0,.18))"/>
    <path d="M117 442l5 5 5-5z" fill="#fff"/>
    <text x="79" y="393" font-size="11" font-weight="600" fill="var(--ink)">2021-10-29</text>
    <text x="79" y="408" font-size="8.5" fill="var(--green)">Crestpoint: 700</text>
    <text x="79" y="420" font-size="8.5" fill="var(--red)">Northline: 668</text>
    <text x="79" y="432" font-size="8.5" fill="var(--blue)">Keystone: 703</text>
  </g>
  <g font-size="11" font-weight="500" fill="var(--ink)">
    <text x="1060" y="387">Northline</text>
    <text x="1060" y="413">Crestpoint</text>
    <text x="1060" y="439">Keystone</text>
  </g>
  <line x1="1135" y1="383" x2="1154" y2="383" stroke="var(--red)" stroke-width="1.5"/>
  <line x1="1135" y1="410" x2="1154" y2="410" stroke="var(--green)" stroke-width="1.5"/>
  <line x1="1135" y1="436" x2="1154" y2="436" stroke="var(--blue)" stroke-width="1.5"/>
</svg>

<div class="axis-x">Credit Pull Date</div>

<footer class="footer">
  <div class="copy">Copyright 2022 by Bravo Ledger Path Tracker</div>
  <div class="addr">418 Harbor Lane, Suite 210, Millbrook, Oregon 97012</div>
  <div class="social"><i></i><i></i><i></i></div>
  <div class="legal">Terms Of Use &nbsp;|&nbsp; Privacy Statement</div>
</footer>
</body>
</html>
```